Brightwater Dental
Stationary for Pediatric Dental & Orthodontics - Health
Stationary for Pediatric Dental & Orthodontics
Bright & Fun-filled
Pediatrics & Orthodontics
Larkspur Hollow Prof. Center 48517 Larkspur Hollow Ave. Suite B-07 Gaithersburg, MD 20886
info@brightwaterdental.org
www.brightwaterdental.org
I have uploaded the co logo to use for the card. I am looking for biz card (2 sided), appointment card, rewards biz card (can explain later, but basically the biz card with an offer on the back), referral pad, envelope (1 sided-no flap work), letterhead, & folder. I would also like to have a QR code linked to the company website on all materials, if it can be color and still work that would be great. I uploaded the static code that I have currently.
This only needs to be on the back of the biz card not the other materials........... Helping Children Who Need: Fillings, Braces, Crowns, Laughing Gas, Whitening, Mouthguards, Hospital Care, Special Needs Care, Clearvane, Nightguards, Cosmetics, Extractions, Walk-in Emergencies, Dental Home.................... Carewell and Most Insurances Accepted

```html
<!DOCTYPE html>
<html lang="en">
<head>
<meta charset="utf-8">
<title>Brightwater Dental – Business Card</title>
<link href="https://fonts.googleapis.com/css2?family=Open+Sans:ital,wght@0,400;0,600;0,700;1,400;1,600&display=swap" rel="stylesheet">
<style>
  :root {
    --backdrop: #e4e5e7;
    --card: #ffffff;
    --brand-blue: #1f5aa6;
    --brand-blue-deep: #17478a;
    --brand-green: #8cc63f;
    --ink: #3b4250;
    --ink-soft: #6b7280;
    --shadow: rgba(30, 40, 60, 0.18);
  }
  * { margin: 0; padding: 0; box-sizing: border-box; }
  html, body {
    width: 1200px; height: 939px; overflow: hidden;
    background: var(--backdrop);
    font-family: "Open Sans", Arial, sans-serif;
    color: var(--ink);
  }
  .stage { position: relative; width: 1200px; height: 939px; }

  .card {
    position: absolute;
    width: 560px; height: 320px;
    background: var(--card);
    box-shadow: 0 14px 30px var(--shadow);
    overflow: hidden;
  }
  .card--front { left: 560px; top: 130px; }
  .card--back  { left: 80px;  top: 490px; }

  .brand { display: flex; flex-direction: column; }
  .brand__row { display: flex; align-items: center; gap: 10px; }
  .brand__dot {
    width: 16px; height: 16px; border-radius: 50%;
    background: var(--brand-blue);
  }
  .brand__name {
    font-weight: 700; color: var(--brand-blue);
    letter-spacing: 0.5px; text-transform: uppercase;
  }
  .brand__tagline {
    color: var(--brand-green); font-weight: 600;
    letter-spacing: 0.6px;
  }

  .card--front .brand {
    position: absolute; left: 50%; top: 50%;
    transform: translate(-50%, -50%); align-items: center;
  }
  .card--front .brand__name { font-size: 30px; }
  .card--front .brand__tagline { font-size: 12px; margin-top: 2px; }

  .card--back .brand { position: absolute; left: 34px; top: 30px; }
  .card--back .brand__name { font-size: 21px; }
  .card--back .brand__dot { width: 12px; height: 12px; }
  .card--back .brand__tagline { font-size: 9px; margin-left: 22px; }

  .address {
    position: absolute; left: 34px; top: 96px;
    font-size: 10px; line-height: 1.55; color: var(--ink-soft);
  }

  .contact {
    position: absolute; right: 34px; top: 120px; text-align: right;
  }
  .contact__name {
    font-size: 15px; font-weight: 600; font-style: italic; color: var(--brand-blue);
  }
  .contact__role {
    font-size: 11px; font-style: italic; color: var(--ink-soft); margin-bottom: 10px;
  }
  .contact__line {
    display: flex; justify-content: flex-end; align-items: center; gap: 6px;
    font-size: 10px; line-height: 1.7; color: var(--ink);
  }
  .contact__line svg { width: 9px; height: 9px; fill: var(--brand-blue); }

  .swoosh { position: absolute; left: 0; bottom: 0; width: 560px; height: 120px; }
  .website {
    position: absolute; right: 30px; bottom: 22px;
    font-size: 11px; font-style: italic; color: #ffffff; letter-spacing: 0.3px;
  }
</style>
</head>
<body>
<main class="stage">

  <section class="card card--front" aria-label="Business card front">
    <div class="brand">
      <div class="brand__row">
        <span class="brand__dot"></span>
        <span class="brand__name">Brightwater Dental</span>
      </div>
      <span class="brand__tagline">Pediatrics &amp; Orthodontics</span>
    </div>
  </section>

  <section class="card card--back" aria-label="Business card back">
    <div class="brand">
      <div class="brand__row">
        <span class="brand__dot"></span>
        <span class="brand__name">Brightwater Dental</span>
      </div>
      <span class="brand__tagline">Pediatrics &amp; Orthodontics</span>
    </div>

    <address class="address" style="font-style:normal">
      48517 Larkspur Ave.<br>
      Suite B-07<br>
      Gaithersburg, MD
    </address>

    <div class="contact">
      <div class="contact__name">Marla Tenwick</div>
      <div class="contact__role">Consultant</div>
      <div class="contact__line">014 582 3097
        <svg viewBox="0 0 10 10"><path d="M2 0.5 L3.6 0.5 L4.3 2.8 L3.2 3.7 Q4.2 5.8 6.3 6.8 L7.2 5.7 L9.5 6.4 L9.5 8 Q9.5 9.5 8 9.5 Q0.5 9 0.5 2 Q0.5 0.5 2 0.5Z"/></svg>
      </div>
      <div class="contact__line">014 582 3098
        <svg viewBox="0 0 10 10"><rect x="0.5" y="2" width="9" height="6.5" rx="1"/><rect x="2.5" y="0.5" width="5" height="2.5" fill="#fff"/></svg>
      </div>
      <div class="contact__line">info@brightwaterdental.org
        <svg viewBox="0 0 10 10"><path d="M0.5 2 H9.5 V8.5 H0.5Z M0.5 2 L5 5.5 L9.5 2" stroke="#fff" stroke-width="0.8"/></svg>
      </div>
    </div>

    <svg class="swoosh" viewBox="0 0 560 120" preserveAspectRatio="none" aria-hidden="true">
      <path d="M0 10 C140 40 300 70 560 60 L560 120 L0 120Z" fill="var(--brand-green)"/>
      <path d="M0 28 C150 60 320 88 560 78 L560 120 L0 120Z" fill="#ffffff"/>
      <path d="M0 36 C160 70 330 96 560 84 L560 120 L0 120Z" fill="var(--brand-blue)"/>
    </svg>
    <span class="website">www.brightwaterdental.org</span>
  </section>

</main>
</body>
</html>
```